Kentucky residential recovery center needs a flyer design

We need a flyer design for a 16 bed male residential/inpatient recovery center based in Richmond, Kentucky. The facility provides short term (average 30 day) treatment to those struggling with substace abuse and addiction. The design should communicate trust, assurance, safety.
Our wesite provides more information https://brovalcare.org/treatment-services/residential-treatment/

Target Market(s)

Men (typically 30-50) struggling with substance addiction

```html
<!DOCTYPE html>
<html lang="en">
<head>
<meta charset="utf-8">
<title>Broval Care – Residential/Inpatient Treatment Flyer</title>
<link href="https://fonts.googleapis.com/css2?family=Poppins:wght@400;500;600;700&family=Roboto+Slab:wght@700;800&display=swap" rel="stylesheet">
<style>
  :root{
    --navy:#25236b;
    --green:#3cb54a;
    --white:#ffffff;
    --ink:#1d1d2b;
    --stage:#d6d6d6;
    --photo-dark:#3f3d3d;
    --photo-mid:#6b6866;
  }
  *{box-sizing:border-box;margin:0;padding:0}
  html,body{width:1197px;height:1200px;overflow:hidden;background:var(--stage)}
  body{display:flex;align-items:center;justify-content:center;font-family:"Poppins",sans-serif}
  .flyer{position:relative;width:820px;height:1160px;background:var(--white);overflow:hidden;box-shadow:0 6px 24px rgba(0,0,0,.18)}
  .slab{font-family:"Roboto Slab",Georgia,serif}

  /* hero */
  .hero{position:absolute;left:0;top:0;width:820px;height:440px;
    background:radial-gradient(ellipse at 78% 70%,#8a8682 0%,transparent 45%),linear-gradient(115deg,var(--photo-dark) 0%,var(--photo-mid) 55%,#4b4847 100%)}
  .hero-shade{position:absolute;inset:0;background:linear-gradient(90deg,rgba(40,38,38,.55),rgba(40,38,38,.15))}
  .hero-title{position:absolute;left:34px;top:36px;color:var(--white);font-size:44px;line-height:56px;font-weight:700}
  .hero-intro{position:absolute;left:34px;top:158px;width:452px;color:var(--white);font-size:15.5px;line-height:20px}
  .pill-green{position:absolute;left:33px;top:261px;width:421px;height:70px;background:var(--green);border-radius:14px 14px 0 0;padding:10px 18px;color:var(--white)}
  .pill-green strong{display:block;font-size:28px;font-weight:700;line-height:34px}
  .pill-green span{display:block;font-size:13px;line-height:16px}
  .pill-navy{position:absolute;left:33px;top:330px;width:502px;height:70px;background:var(--navy);border-radius:0 14px 14px 14px;padding:8px 18px;color:var(--white);font-size:20.5px;font-weight:500;line-height:26px}

  .brand-tab{position:absolute;left:544px;top:0;width:243px;height:266px;background:var(--white);border-radius:0 0 122px 122px;display:flex;flex-direction:column;align-items:center;justify-content:center;gap:12px}
  .brand-dot{width:62px;height:62px;border-radius:50%;background:var(--navy)}
  .brand-name{font-size:24px;font-weight:700;color:var(--navy)}

  /* issues */
  .issues{position:absolute;left:0;top:434px;width:820px;height:276px;background:var(--green)}
  .issues-notch{position:absolute;left:0;top:0}
  .tag{position:absolute;display:inline-block;font-size:15.5px;color:var(--white);padding:5px 13px;border-radius:8px;line-height:20px;white-space:nowrap}
  .tag-navy{background:var(--navy);left:50%;transform:translateX(-50%);top:41px}
  .issues-heading{position:absolute;left:0;right:0;top:80px;text-align:center;color:var(--white);font-size:33px;line-height:40px}
  .cards{position:absolute;left:33px;top:160px;display:flex;gap:15px}
  .card{position:relative;width:177px;height:90px;background:var(--white);border-radius:12px;display:flex;align-items:center;justify-content:center;text-align:center;padding-top:14px;font-family:"Roboto Slab",Georgia,serif;font-weight:700;font-size:15.5px;line-height:20px;color:var(--ink)}
  .card-icon{position:absolute;top:-32px;left:50%;transform:translateX(-50%);width:60px;height:60px;border-radius:50%;background:var(--navy);border:3px solid var(--white);box-shadow:0 0 0 1px #cfd0dc;display:flex;align-items:center;justify-content:center}

  /* process */
  .process{position:absolute;left:0;top:710px;width:820px;height:358px;background:var(--navy)}
  .tag-green{background:var(--green);left:33px;top:27px}
  .process-heading{position:absolute;left:34px;top:70px;color:var(--white);font-size:33px;line-height:40px}
  .steps{position:absolute;left:33px;top:130px;width:412px;list-style:none}
  .step{display:flex;align-items:flex-start;gap:15px;color:var(--white);font-size:14.5px;line-height:18px;margin-bottom:20px}
  .step svg{flex:none;width:40px;height:40px;margin-top:2px}
  .photo{position:absolute;border-radius:50%;border:4px solid var(--white)}
  .photo-room{left:544px;top:48px;width:245px;height:245px;background:radial-gradient(circle at 55% 60%,#2a2a2e 0%,#55504b 35%,#cfc7bc 60%,#e6e1d9 100%)}
  .photo-guest{left:455px;top:125px;width:178px;height:178px;background:linear-gradient(180deg,#7aa2c8 0%,#9db6c9 45%,#8c8f94 70%,#6d5a48 100%)}

  /* footer */
  .footer{position:absolute;left:0;top:1068px;width:820px;height:92px;display:flex;align-items:center;padding:0 33px;justify-content:space-between}
  .contact{display:flex;align-items:center;gap:10px;font-size:16px;color:var(--ink);white-space:nowrap}
  .contact svg{width:44px;height:44px;flex:none}
  .contact b{font-weight:600}
  .accent{color:var(--green)}
</style>
</head>
<body>
<main class="flyer">
  <section class="hero">
    <div class="hero-photo" role="img" aria-label="Photo of a softly lit bedroom in the residential center" style="position:absolute;inset:0"></div>
    <div class="hero-shade"></div>
    <h1 class="hero-title slab">Residential/Inpatient<br>Trratment</h1>
    <p class="hero-intro">Impatient treatment, also referredto as residential treatment, provides the highest level of rehav services for patients diagnosed with alcohol, or other drug or substance addiction.</p>
    <div class="pill-green"><strong>30 DAYS TREATMENT</strong><span>to those struggling with substace abuse and addiction.</span></div>
    <div class="pill-navy">16 bed male residential/inpatient recovery center based in Richmond, Kentucky.</div>
    <div class="brand-tab">
      <div class="brand-dot"></div>
      <div class="brand-name">Broval Care</div>
    </div>
  </section>

  <section class="issues">
    <svg class="issues-notch" width="820" height="24" viewBox="0 0 820 24"><path d="M0 0H820V6L410 22L0 6Z" fill="#ffffff"/></svg>
    <span class="tag tag-navy">PROBLEMS WE CAN HELP WITH</span>
    <h2 class="issues-heading slab">WHAT ISSUES CAN BE TREATED?</h2>
    <div class="cards">
      <div class="card"><span class="card-icon"><svg width="30" height="30" viewBox="0 0 30 30"><g transform="rotate(45 15 15)" fill="#fff"><rect x="12.5" y="3" width="5" height="7" rx="1"/><rect x="10" y="10" width="10" height="17" rx="3"/></g></svg></span>ALCOHOLISM</div>
      <div class="card"><span class="card-icon"><svg width="32" height="32" viewBox="0 0 32 32" fill="#fff"><g transform="rotate(45 12 16)"><rect x="9.5" y="6" width="5" height="16" rx="1"/><rect x="11.3" y="22" width="1.4" height="7"/><rect x="7.5" y="4" width="9" height="2.5"/></g><rect x="20" y="17" width="8" height="11" rx="2"/><rect x="22" y="14" width="4" height="3"/></svg></span>DRUG<br>ADDICTION</div>
      <div class="card"><span class="card-icon"><svg width="30" height="30" viewBox="0 0 30 30"><g transform="rotate(-45 15 15)"><rect x="4" y="10" width="22" height="10" rx="5" fill="#fff"/><rect x="15" y="11.5" width="9.5" height="7" rx="3.5" fill="#25236b"/></g></svg></span>MEDICATION<br>ADDICTION</div>
      <div class="card"><span class="card-icon"><svg width="30" height="30" viewBox="0 0 30 30" fill="none" stroke="#fff" stroke-width="2"><circle cx="15" cy="13" r="9"/><path d="M9 21v6M21 21v6"/><path d="M11 12h8M15 8v9"/></svg></span>BEHAVIORAL<br>HEALTH</div>
    </div>
  </section>

  <section class="process">
    <span class="tag tag-green">STAGES OF RESIDENTIAL RECOVERY PROCESS</span>
    <h2 class="process-heading slab">HOW DOES IT WORK?</h2>
    <ol class="steps">
      <li class="step"><svg viewBox="0 0 40 40" fill="#3cb54a"><path d="M16 6h16a6 6 0 0 1 6 6v6a6 6 0 0 1-6 6h-2l4 5-9-5h-9a6 6 0 0 1-6-6v-6a6 6 0 0 1 6-6z" opacity=".75"/><path d="M8 14h16a6 6 0 0 1 6 6v6a6 6 0 0 1-6 6H14l-9 5 4-5H8a6 6 0 0 1-6-6v-6a6 6 0 0 1 6-6z"/><circle cx="10" cy="23" r="2" fill="#25236b"/><circle cx="16" cy="23" r="2" fill="#25236b"/><circle cx="22" cy="23" r="2" fill="#25236b"/></svg><span>Speak with our team in private about the nature of your challenges and what you need help with</span></li>
      <li class="step"><svg viewBox="0 0 40 40" fill="#3cb54a"><circle cx="20" cy="11" r="8"/><path d="M4 38c0-10 7-15 16-15s16 5 16 15z"/><path d="M14 24v6a3 3 0 0 0 6 0" fill="none" stroke="#25236b" stroke-width="2"/><circle cx="27" cy="31" r="2.5" fill="#25236b"/></svg><span>Together we select an appropriate time slot to book you in for an induction appointment with one of our clinical staff</span></li>
      <li class="step"><svg viewBox="0 0 40 40"><circle cx="20" cy="20" r="17" fill="none" stroke="#3cb54a" stroke-width="3"/><path d="M16 12l11 8-11 8z" fill="#3cb54a"/></svg><span>Once the induction is completed, we'll schedule you in to commence your inpatient program</span></li>
    </ol>
    <div class="photo photo-room" role="img" aria-label="Photo of the center's meeting room with a long table and chairs"></div>
    <div class="photo photo-guest" role="img" aria-label="Photo of a program graduate holding a certificate outdoors"></div>
  </section>

  <footer class="footer">
    <div class="contact"><svg viewBox="0 0 44 44"><circle cx="22" cy="22" r="19.5" fill="none" stroke="#3cb54a" stroke-width="3"/><path d="M15 13l4-1 2 6-3 2c1 3 3 5 6 6l2-3 6 2-1 4c-9 1-17-7-16-16z" fill="#25236b"/></svg><b>(859) 555-0142</b></div>
    <div class="contact"><svg viewBox="0 0 44 44"><circle cx="22" cy="22" r="19.5" fill="none" stroke="#3cb54a" stroke-width="3"/><rect x="12" y="15" width="20" height="14" rx="1.5" fill="#25236b"/><path d="M12.5 16l9.5 7 9.5-7" fill="none" stroke="#fff" stroke-width="1.5"/></svg><span>admissions@<span class="accent">brovalcare</span>.com</span></div>
    <div class="contact"><svg viewBox="0 0 44 44"><circle cx="22" cy="22" r="19.5" fill="none" stroke="#3cb54a" stroke-width="3"/><g fill="none" stroke="#25236b" stroke-width="2"><circle cx="22" cy="22" r="10"/><ellipse cx="22" cy="22" rx="4.5" ry="10"/><path d="M12 22h20M14 17h16M14 27h16"/></g></svg><span>www.<span class="accent">brovalcare</span>.org</span></div>
  </footer>
</main>
</body>
</html>
```